Carpet cleaning company focused on high quality needs business cards

We are a growing company that just merged with another company and need to design a new business card. We do both residential as well as commercial cleaning. We do carpet, tile & grout, upholstery, hard floors, and stain & pet odor removal. We treat our customers like family and strive to achieve outstanding results with every job.

```html
<!DOCTYPE html>
<html lang="en">
<head>
<meta charset="utf-8">
<title>Marlow Floor Care – Business Card</title>
<link rel="stylesheet" href="https://fonts.googleapis.com/css2?family=Open+Sans:wght@400;600;700;800&display=swap">
<style>
  :root {
    --page-bg: #d9d2c8;
    --card-bg: #f1e9df;
    --ink: #231f1e;
    --text: #2b2b2b;
    --teal: #1d6f8e;
    --red: #d63a32;
    --art-blue: #2f7f94;
    --art-tan: #c9a063;
  }
  html, body {
    margin: 0;
    width: 1200px;
    height: 1047px;
    overflow: hidden;
    background: var(--page-bg);
    font-family: "Open Sans", Arial, sans-serif;
  }
  .card {
    position: absolute;
    left: 100px;
    top: 250px;
    width: 1000px;
    height: 548px;
    background: var(--card-bg);
    border-radius: 22px;
    overflow: hidden;
    box-shadow: 0 10px 30px rgba(0,0,0,0.15);
  }
  .accent-band {
    position: absolute;
    left: 0;
    top: 0;
    width: 1000px;
    height: 548px;
  }
  .mascot-art {
    position: absolute;
    left: 48px;
    top: 6px;
    width: 386px;
    height: 524px;
    background: linear-gradient(180deg, var(--art-blue) 0%, var(--art-blue) 55%, var(--art-tan) 100%);
    opacity: 0.5;
    border-radius: 12px;
  }
  .brand {
    position: absolute;
    right: 37px;
    top: 112px;
    margin: 0;
    color: var(--ink);
    font-size: 46px;
    font-weight: 700;
    line-height: 1;
    white-space: nowrap;
  }
  .person {
    position: absolute;
    right: 48px;
    top: 240px;
    margin: 0;
    font-size: 31px;
    font-weight: 700;
    letter-spacing: 0.5px;
    white-space: nowrap;
  }
  .person .first { color: var(--teal); }
  .person .last { color: var(--red); }
  .person-bar {
    position: absolute;
    right: 0;
    top: 251px;
    width: 20px;
    height: 58px;
    background: var(--red);
  }
  .role {
    position: absolute;
    right: 48px;
    top: 285px;
    margin: 0;
    font-size: 22px;
    color: var(--text);
  }
  .address {
    position: absolute;
    right: 48px;
    top: 336px;
    margin: 0;
    font-style: normal;
    font-size: 22px;
    line-height: 31px;
    text-align: right;
    color: var(--text);
  }
  .channels {
    position: absolute;
    right: 37px;
    top: 416px;
    margin: 0;
    padding: 0;
    list-style: none;
    font-size: 22px;
    line-height: 32.5px;
    text-align: right;
    color: var(--text);
  }
  .channels li { display: flex; justify-content: flex-end; align-items: center; gap: 8px; }
  .channels svg { width: 19px; height: 19px; fill: var(--teal); }
</style>
</head>
<body>
  <article class="card">
    <svg class="accent-band" viewBox="0 0 1000 548" aria-hidden="true">
      <polygon points="0,399 498,257 498,548 0,548" fill="var(--red)"/>
    </svg>
    <div class="mascot-art" role="img" aria-label="Cartoon cleaner in cap holding a steam cleaning wand with sunburst behind"></div>

    <h1 class="brand">Marlow Floor Care</h1>

    <p class="person"><span class="first">DANA</span> <span class="last">MORVEN</span></p>
    <div class="person-bar"></div>
    <p class="role">Executive Director</p>

    <address class="address">2170 Harbor Way<br>Lake Orrin,</address>

    <ul class="channels">
      <li>123 456 789
        <svg viewBox="0 0 24 24" aria-label="phone"><path d="M6.6 10.8a15.1 15.1 0 0 0 6.6 6.6l2.2-2.2a1 1 0 0 1 1-.25 11.4 11.4 0 0 0 3.6.57 1 1 0 0 1 1 1V20a1 1 0 0 1-1 1A17 17 0 0 1 3 4a1 1 0 0 1 1-1h3.5a1 1 0 0 1 1 1c0 1.25.2 2.450.57 3.57a1 1 0 0 1-.25 1z"/></svg>
      </li>
      <li>info@marlowfloor.com
        <svg viewBox="0 0 24 24" aria-label="email"><path d="M3 5h18v14H3z"/><path d="M3 5l9 7 9-7" fill="none" stroke="#f1e9df" stroke-width="2"/></svg>
      </li>
      <li>www.marlowfloor.com
        <svg viewBox="0 0 24 24" aria-label="website"><circle cx="12" cy="12" r="10"/><path d="M2 12h20M12 2c3 3 3 17 0 20M12 2c-3 3-3 17 0 20" fill="none" stroke="#f1e9df" stroke-width="1.5"/></svg>
      </li>
    </ul>
  </article>
</body>
</html>
```